Design and Renovation Company Luxury Business Card

I want to create a luxury business card for a Design and Renovation Firm . We will use our current logo. The company name is 742BUILD. We do not want anything standard. We need a very unique concept.
Please see uploaded inspiration. I really like the textured paper option. I would like the card to be thick with debossing, and/or embossing options. The logo has orange in it but I would like to see the card with and without the orange. I think the orange may make the company feel less high-end. The goal is to elevate the logo not match its vibe per se of the logo. We want something very unique, not standard at all!
I would like a space for :
Logo,
Name,
Position,
Email,
Office number,
Website Address,
Business Address,
Thank you!
Have fun!
Target Market(s)
Home owners Age 35 +
Industry/Entity Type
Design and Renovation
Contact Information for Business Card
Logo, Name, Position, Email, Office number, Website Address, Business Address,.
Colors
Designer to choose colors to be used in the design.
Requirements
Must have
- A luxury designer feel. Must be black or dark grey but open to other luxury ideas.
Nice to have
- Gold, silver, black embossing or debossing. Textured paper design.
Should not have
- A cheap look and feel.

```html
<!DOCTYPE html>
<html lang="en">
<head>
<meta charset="utf-8">
<title>742BUILD Business Card</title>
<link rel="stylesheet" href="https://fonts.googleapis.com/css2?family=Open+Sans:wght@400;600;700&display=swap">
<style>
  :root {
    --page-bg: #e4e4e4;
    --orange: #f6921e;
    --ink: #111111;
    --card-black: #0a0a0a;
    --white: #ffffff;
    --gold: #e9c65b;
    --gold-rule: #d8b848;
  }
  * { box-sizing: border-box; margin: 0; padding: 0; }
  html, body {
    width: 1135px;
    height: 1200px;
    overflow: hidden;
    background: var(--page-bg);
    font-family: "Open Sans", Arial, sans-serif;
  }
  .sheet {
    width: 1135px;
    height: 1200px;
    display: flex;
    flex-direction: column;
    align-items: center;
    justify-content: space-evenly;
  }
  .card {
    position: relative;
    width: 960px;
    height: 549px;
  }
  .card--front { background: var(--orange); color: var(--ink); }
  .card--back { background: var(--card-black); color: var(--gold); }

  .brand {
    position: absolute;
    left: 0; right: 0;
    display: flex;
    align-items: center;
    justify-content: center;
    gap: 18px;
    font-weight: 700;
    letter-spacing: 3px;
  }
  .brand__square { display: block; flex: none; }
  .card--front .brand { top: 215px; font-size: 76px; color: var(--ink); }
  .card--front .brand__square { width: 58px; height: 58px; background: var(--white); }
  .card--back .brand { top: 70px; font-size: 48px; color: var(--white); letter-spacing: 2px; gap: 12px; }
  .card--back .brand__square { width: 30px; height: 30px; background: var(--orange); }

  .identity {
    position: absolute;
    top: 222px; left: 0; right: 0;
    text-align: center;
    line-height: 1.3;
  }
  .identity__company { font-size: 27px; font-weight: 700; }
  .identity__tagline { font-size: 27px; font-weight: 400; }
  .identity__role { font-size: 21px; margin-top: 4px; }

  .contact {
    position: absolute;
    top: 390px; left: 0; right: 0;
    text-align: center;
    font-size: 21px;
    line-height: 1.55;
  }

  .footer-rule {
    position: absolute;
    left: 0; right: 0;
    top: 498px;
    display: flex;
    align-items: center;
    gap: 12px;
    font-size: 21px;
    white-space: nowrap;
  }
  .footer-rule::before, .footer-rule::after {
    content: "";
    flex: 1;
    height: 3px;
  }
  .card--front .footer-rule::before, .card--front .footer-rule::after { background: var(--ink); }
  .card--back .footer-rule::before, .card--back .footer-rule::after { background: var(--gold-rule); }
</style>
</head>
<body>
<main class="sheet">
  <section class="card card--front" aria-label="Card front">
    <div class="brand"><span class="brand__square"></span>742BUILD</div>
    <p class="footer-rule">www.742builddesign and renovation firm.com</p>
  </section>

  <section class="card card--back" aria-label="Card back">
    <div class="brand"><span class="brand__square"></span>742BUILD</div>
    <div class="identity">
      <p class="identity__company">742BUILD DESIGN</p>
      <p class="identity__tagline">and renovation firm</p>
      <p class="identity__role">Ceo</p>
    </div>
    <div class="contact">
      <p>+ 1234567890</p>
      <p>Dummy City, Dummy Country</p>
    </div>
    <p class="footer-rule">info@742builddesign and renovation firm.com</p>
  </section>
</main>
</body>
</html>
```